Brightwater Commerce Business Card Design

Hello,

Attached you will find our logo. We are looking for a sharp business card design.

Other info to be included is:
Name: Marcus Delaney
Title: CEO
Office: (555) 382-7146
Cell: (555) 382-7146
E-mail address: marcus@brightwatercommerce.example
website: www.BrightwaterCommerce.example

```html
<!DOCTYPE html>
<html lang="en">
<head>
<meta charset="utf-8">
<title>Brightwater Commerce – Business Card</title>
<link rel="stylesheet" href="https://fonts.googleapis.com/css2?family=Open+Sans:wght@400;700&family=Arimo:wght@400&display=swap">
<style>
  :root {
    --backdrop: #e9e7e4;
    --card-white: #ffffff;
    --brand-blue: #1457a3;
    --brand-red: #e0393f;
    --soft-blue: #5b7fc0;
    --text-white: #ffffff;
    --wordmark: #1d5fae;
  }
  html, body {
    margin: 0;
    padding: 0;
    width: 1200px;
    height: 1200px;
    overflow: hidden;
    background: var(--backdrop);
  }
  .canvas {
    position: relative;
    width: 1200px;
    height: 1200px;
  }
  .business-card {
    position: absolute;
    left: 100px;
    top: 308px;
    width: 1000px;
    height: 584px;
    box-shadow: 0 6px 18px rgba(0,0,0,0.18);
  }
  .card-bg { fill: var(--card-white); }
  .shape-blue { fill: var(--brand-blue); }
  .shape-red { fill: var(--brand-red); filter: drop-shadow(0 -3px 6px rgba(0,0,0,0.25)); }
  .shape-soft-blue { fill: var(--soft-blue); }
  .wordmark {
    font-family: "Open Sans", sans-serif;
    font-weight: 700;
    font-size: 26px;
    fill: var(--wordmark);
  }
  .wordmark-mark { fill: var(--wordmark); }
  .contact-name {
    font-family: "Open Sans", sans-serif;
    font-weight: 700;
    font-size: 20px;
    fill: var(--text-white);
    letter-spacing: 0.3px;
  }
  .contact-title {
    font-family: "Open Sans", sans-serif;
    font-weight: 700;
    font-size: 18px;
    fill: var(--text-white);
  }
  .contact-rule { stroke: var(--text-white); stroke-width: 1.5; }
  .contact-line {
    font-family: "Open Sans", sans-serif;
    font-weight: 400;
    font-size: 19px;
    fill: var(--text-white);
  }
  .website {
    font-family: "Arimo", sans-serif;
    font-size: 16.5px;
    fill: var(--text-white);
    letter-spacing: 0.2px;
  }
</style>
</head>
<body>
<main class="canvas">
  <svg class="business-card" viewBox="0 0 805 470" width="1000" height="584" xmlns="http://www.w3.org/2000/svg">
    <defs>
      <clipPath id="card-clip"><rect width="805" height="470"/></clipPath>
    </defs>
    <rect class="card-bg" width="805" height="470"/>
    <g clip-path="url(#card-clip)">
      <circle class="shape-blue" cx="20" cy="400" r="445"/>
      <circle class="shape-soft-blue" cx="840" cy="480" r="185"/>
      <circle class="shape-red" cx="415" cy="602" r="395"/>
    </g>

    <g class="brand">
      <rect class="wordmark-mark" x="456" y="100" width="18" height="18"/>
      <text class="wordmark" x="484" y="118">Brightwater Commerce</text>
    </g>

    <g class="contact">
      <text class="contact-name" x="46" y="263">MARCUS DELANEY</text>
      <text class="contact-title" x="46" y="293">CEO</text>
      <line class="contact-rule" x1="46" y1="302" x2="330" y2="302"/>
      <text class="contact-line" x="46" y="327">Office: (555) 382-7146</text>
      <text class="contact-line" x="46" y="357">Cell: (555) 382-7146</text>
      <text class="contact-line" x="46" y="388">E-mail address: marcus@brightwatercommerce.example</text>
    </g>

    <text class="website" x="400" y="444" text-anchor="middle">WWW.BRIGHTWATERCOMMERCE.EXAMPLE</text>
  </svg>
</main>
</body>
</html>
```